Personal Injury Funding Flyer

We are Qorvale Financial, a provider of receivables management solutions to the surgical industry.
We want a 1 page flyer to showcase our Motor Vehicle Accident (MVA) and Personal Injury (PI) case management and lien purchasing.

Attached is a document:
1- a flyer from a competitor. We like the overall feel of the flyer and the simplicity of the information presented.

You can also check out our website for examples of our company's style
www.qorvalefinancial.example

Target Market(s)

Surgeons, office managers, administrators and CFOS at smaller surgical facilities and surgical hospitals nationwide

Industry/Entity Type

Financial

Requirements
Must have
• Titled: Personal Injury Case Funding
• Tagline: We Ensure Your Cases are Financially Sound
• Include Qorvale Financial's logo
• Be sure to boldly highlight the 3 points:
• 3 Steps to Successful PI Case Management
• 1) Evaluate Cases
• Evaluate the financial aspects of the case including policy limits.
• 2) Consult Attorneys
• Evaluate the case background and likelihood of settlement.
• 3) Guaranteed Funding
• 15 day funding on most cases.
• How Does MVA/PI Funding Work?
• We pay you upfront and wait for the case to settle.
• Our funding eliminates the risk, hassle and uncertainty associated with PI cases.
• You get paid 100% NON-RECOURSE
• Include contact phone number (800) 555-0147
• >No Hassles
• >No Risk
• >Guaranteed Funds.
Nice to have
• Smiling doctor picture
Should not have
• Too much information

```html
<!DOCTYPE html>
<html lang="en">
<head>
<meta charset="utf-8">
<title>Qorvale Financial – Personal Injury Case Funding</title>
<link rel="stylesheet" href="https://fonts.googleapis.com/css2?family=Open+Sans:ital,wght@0,400;0,600;0,700;1,400;1,600&display=swap">
<style>
  :root {
    --navy: #2c3a6c;
    --navy-deep: #151b35;
    --red: #a3403b;
    --maroon: #4b1818;
    --grey: #6f6f70;
    --grey-light: #c9c9c9;
    --ink: #1b1b1b;
    --muted: #555;
    --white: #ffffff;
  }
  * { margin: 0; padding: 0; box-sizing: border-box; }
  html, body { width: 848px; height: 1200px; overflow: hidden; background: var(--white); }
  body { font-family: "Open Sans", Arial, sans-serif; color: var(--ink); }
  .flyer { position: relative; width: 848px; height: 1200px; }

  .brand-bar { position: absolute; top: 0; left: 0; width: 848px; height: 130px; }
  .brand { position: absolute; left: 208px; top: 44px; display: flex; align-items: center; gap: 12px; }
  .brand-mark { width: 36px; height: 36px; background: var(--maroon); }
  .brand-name { font-size: 29px; font-weight: 700; color: var(--grey); white-space: nowrap; }
  .brand-divider { position: absolute; left: 571px; top: 40px; width: 1px; height: 64px; background: var(--grey-light); }
  .brand-service { position: absolute; left: 596px; top: 37px; font-size: 17px; line-height: 23px; font-weight: 600; }
  .brand-service span { display: block; }
  .brand-service .s1 { color: var(--maroon); }
  .brand-service .s2 { color: var(--navy-deep); }
  .brand-service .s3 { color: var(--grey); }

  .hero-photo { position: absolute; top: 130px; left: 0; width: 848px; height: 398px;
    background: linear-gradient(100deg, #e9eef1 0%, #d9e3e8 40%, #cfe0e8 60%, #eef2f4 100%); }
  .hero-title { position: absolute; top: 130px; left: 0; width: 468px; height: 212px;
    background: linear-gradient(90deg, rgba(44,58,108,0.93) 0 232px, rgba(163,64,59,0.9) 232px 100%);
    color: var(--white); padding: 16px 0 0 14px; }
  .hero-title h1 { font-size: 40px; line-height: 48px; font-weight: 700; letter-spacing: 0.3px; }
  .hero-title p { margin-top: 12px; font-size: 14.5px; letter-spacing: 0.2px; }

  .steps { position: absolute; top: 528px; left: 0; width: 848px; height: 250px; }
  .step { position: absolute; top: 0; width: 250px; text-align: center; }
  .step-1 { left: 20px; } .step-2 { left: 305px; } .step-3 { left: 583px; }
  .step-num { font-size: 112px; font-weight: 700; line-height: 118px; letter-spacing: -3px; }
  .step-head { margin-top: 8px; font-size: 20px; }
  .step-text { font-size: 16px; line-height: 24px; }
  .step-1 .step-num, .step-1 .step-head { color: var(--navy-deep); }
  .step-2 .step-num, .step-2 .step-head { color: var(--maroon); }
  .step-3 .step-num, .step-3 .step-head { color: var(--grey); }
  .step-rule { position: absolute; top: 90px; width: 1px; height: 152px; background: var(--grey-light); }
  .rule-a { left: 287px; } .rule-b { left: 575px; }

  .how { position: absolute; top: 838px; left: 0; width: 848px; text-align: center; }
  .how h2 { font-size: 44px; line-height: 70px; font-weight: 700; color: var(--ink); }
  .how p { font-size: 19.5px; font-style: italic; color: var(--muted); }
  .how .p1 { margin-top: 4px; } .how .p2 { margin-top: 14px; }
  .recourse { position: absolute; top: 1022px; left: 0; width: 848px; text-align: center;
    font-size: 36px; color: var(--maroon); letter-spacing: 0.5px; }

  .pill { position: absolute; top: 1108px; height: 50px; border-radius: 25px; color: var(--white);
    font-size: 30px; font-style: italic; display: flex; align-items: center; justify-content: center; white-space: nowrap; }
  .pill-1 { left: 8px; width: 270px; background: var(--navy-deep); }
  .pill-2 { left: 289px; width: 271px; background: var(--maroon); }
  .pill-3 { left: 568px; width: 272px; background: var(--grey); }

  .footer { position: absolute; top: 1166px; left: 0; width: 848px; height: 34px; display: flex;
    color: var(--white); font-size: 16px; }
  .footer div { display: flex; align-items: center; justify-content: center; }
  .footer .phone { width: 435px; background: var(--navy); }
  .footer .web { flex: 1; background: var(--red); }
</style>
</head>
<body>
<div class="flyer">
  <header class="brand-bar">
    <div class="brand"><div class="brand-mark"></div><div class="brand-name">Qorvale Financial</div></div>
    <div class="brand-divider"></div>
    <div class="brand-service"><span class="s1">Receivable</span><span class="s2">Management</span><span class="s3">Solutions</span></div>
  </header>

  <div class="hero-photo" role="img" aria-label="Smiling doctor with stethoscope in front of a blurred medical team"></div>
  <div class="hero-title">
    <h1>PERSONAL<br>INJURY CASE<br>FUNDING</h1>
    <p>WE ENSURE YOUR CASES ARE FINANCIALLY SOUND</p>
  </div>

  <section class="steps">
    <div class="step step-1"><div class="step-num">1.</div><div class="step-head">Evaluate Cases</div><div class="step-text">Evaluate the financial aspects<br>of the case including policy<br>limits.</div></div>
    <div class="step-rule rule-a"></div>
    <div class="step step-2"><div class="step-num">2.</div><div class="step-head">Consult Attorneys</div><div class="step-text">Evaluate the case background<br>and likelihood of settlement.</div></div>
    <div class="step-rule rule-b"></div>
    <div class="step step-3"><div class="step-num">3.</div><div class="step-head">Guaranteed Funding</div><div class="step-text">15 day funding on most cases.</div></div>
  </section>

  <section class="how">
    <h2>How Does MVA/PI Funding Work?</h2>
    <p class="p1">We pay you upfront and wait for the case to settle.</p>
    <p class="p2">Our funding eliminates the risk, hassle and uncertainty associated with PI cases.</p>
  </section>
  <div class="recourse">You get paid 100% NON-RECOURSE</div>

  <div class="pill pill-1">No Hassles</div>
  <div class="pill pill-2">No Risk</div>
  <div class="pill pill-3">Guaranteed Funds</div>

  <footer class="footer">
    <div class="phone">CONTACTNUMBER (800) 555-0147</div>
    <div class="web">www.qorvalefinancial.example</div>
  </footer>
</div>
</body>
</html>
```